Dorsey K. Wendell Business Card

We need a business card for our company Dorsey K. Wendell Heating & Plumbing to be distributed to potential customers. It should follow the color scheme of our logo and have a modern upscale and masculine look.

The logo is attached and the info below should also be included:

5187 W. Cedar Brook Rd.
Orchard Falls, PA 17392

Russell T. Wendell
(717) 592-0817
russelltwendell@fernmail.net
dorseykwendell.net
PA #093148

Industry/Entity Type

Business

Contact Information for Business Card

5187 W. Cedar Brook Rd.
Orchard Falls, PA 17392

Russell T. Wendell
(717) 592-0817
russelltwendell@fernmail.net
dorseykwendell.net
PA #093148

Colors

Designer to choose colors to be used in the design.

Requirements
Must have
• Information above included

```html
<!DOCTYPE html>
<html lang="en">
<head>
<meta charset="utf-8">
<title>Dorsey K. Wendell Business Card</title>
<link rel="stylesheet" href="https://fonts.googleapis.com/css2?family=Lato:wght@400;700;900&display=swap">
<style>
  :root {
    --stage: #3a3a3a;
    --brand-blue: #0753a3;
    --brand-blue-deep: #04448a;
    --brand-green: #9acd32;
    --paper: #ffffff;
    --ink-light: #ffffff;
  }
  * { box-sizing: border-box; margin: 0; padding: 0; }
  html, body {
    width: 1200px; height: 900px; overflow: hidden;
    background: var(--stage);
    font-family: "Lato", Arial, sans-serif;
  }
  .stage {
    width: 1200px; height: 900px;
    display: flex; flex-direction: column; align-items: center; justify-content: center;
    gap: 56px;
  }
  .card {
    position: relative;
    width: 620px; height: 354px;
    overflow: hidden;
    box-shadow: 0 10px 30px rgba(0,0,0,.45);
  }
  /* Front */
  .card-front { background: var(--paper); }
  .card-front .swoosh { position: absolute; inset: 0; }
  .front-brand {
    position: absolute; left: 36px; top: 118px; width: 250px;
    display: flex; align-items: flex-start; gap: 12px;
  }
  .brand-square {
    width: 26px; height: 26px; flex: none; margin-top: 4px;
    background: var(--brand-blue);
  }
  .brand-name {
    color: var(--brand-blue);
    font-weight: 900;
    font-size: 21px; line-height: 1.25;
    text-transform: uppercase; letter-spacing: .5px;
  }
  .contact {
    position: absolute; left: 372px; top: 52px;
    color: var(--ink-light);
    font-size: 15px; line-height: 1.38;
  }
  .contact-name {
    color: var(--brand-green);
    font-size: 26px; font-weight: 400;
    margin-bottom: 6px;
  }
  .contact-license { margin-bottom: 10px; }
  .contact-address { margin-bottom: 10px; }
  .contact-lines { list-style: none; }
  .contact-lines li { display: flex; align-items: center; gap: 9px; }
  .contact-lines svg { width: 13px; height: 13px; flex: none; }
  /* Back */
  .card-back {
    background: var(--brand-blue);
    display: flex; flex-direction: column; align-items: center; justify-content: center;
  }
  .back-brand { display: flex; align-items: center; gap: 16px; }
  .back-brand .brand-square { background: var(--ink-light); width: 34px; height: 34px; margin: 0; }
  .back-brand .brand-name { color: var(--ink-light); font-size: 30px; }
  .back-rule { width: 330px; height: 2px; background: var(--brand-green); margin: 16px 0 34px; }
  .back-web { color: var(--ink-light); font-size: 17px; letter-spacing: .5px; }
</style>
</head>
<body>
<main class="stage">

  <section class="card card-front" aria-label="Business card front">
    <svg class="swoosh" viewBox="0 0 620 354" width="620" height="354" aria-hidden="true">
      <path d="M250 354 C252 262 286 172 332 108 C300 190 284 272 290 354 Z" fill="var(--brand-blue)"/>
      <path d="M334 0 L356 0 C306 120 294 240 304 354 L288 354 C274 240 284 112 334 0 Z" fill="var(--brand-green)"/>
      <path d="M358 0 L620 0 L620 354 L306 354 C296 240 308 120 358 0 Z" fill="var(--brand-blue)"/>
    </svg>

    <div class="front-brand">
      <span class="brand-square" aria-hidden="true"></span>
      <p class="brand-name">Dorsey K. Wendell<br>Heating &amp; Plumbing</p>
    </div>

    <div class="contact">
      <h1 class="contact-name">Russell T. Wendell</h1>
      <p class="contact-license">PA #093148</p>
      <p class="contact-address">5187 W. Cedar Brook Rd.<br>Orchard Falls, PA 17392</p>
      <ul class="contact-lines">
        <li>
          <svg viewBox="0 0 16 16" aria-hidden="true"><path d="M3.5 1.5l2.5 0 1 3.5-1.8 1.2c.8 1.8 2.2 3.2 4 4l1.2-1.8 3.5 1v2.5c0 .8-.7 1.5-1.5 1.5C6.8 13.4 2.6 9.2 2 3c0-.8.7-1.5 1.5-1.5z" fill="var(--brand-green)"/></svg>
          <span>(717) 592-0817</span>
        </li>
        <li>
          <svg viewBox="0 0 16 16" aria-hidden="true"><rect x="1" y="3" width="14" height="10" fill="var(--brand-green)"/><path d="M1 3l7 6 7-6" fill="none" stroke="var(--brand-blue)" stroke-width="1.4"/></svg>
          <span>russelltwendell@fernmail.net</span>
        </li>
        <li>
          <svg viewBox="0 0 16 16" aria-hidden="true"><circle cx="8" cy="8" r="7" fill="var(--brand-green)"/><g fill="none" stroke="var(--brand-blue)" stroke-width="1"><ellipse cx="8" cy="8" rx="3" ry="7"/><path d="M1 8h14M2.5 4.5h11M2.5 11.5h11"/></g></svg>
          <span>www.dorseykwendell.net</span>
        </li>
      </ul>
    </div>
  </section>

  <section class="card card-back" aria-label="Business card back">
    <div class="back-brand">
      <span class="brand-square" aria-hidden="true"></span>
      <p class="brand-name">Dorsey K. Wendell<br>Heating &amp; Plumbing</p>
    </div>
    <div class="back-rule" aria-hidden="true"></div>
    <p class="back-web">www.dorseykwendell.net</p>
  </section>

</main>
</body>
</html>
```